Business Card Design

Copperfield Lantern & Spark, Inc. (CLS), located in Memphis, TN began operating on 2003. We are a certified
minority woman-owned business that genuinely takes a vested interest in our customers. We serve utilities,
government, contractors and end user markets in electrical, water, gas and industrial supplies. Our core
competency as a distributor of electrical materials has positioned us to serve business of all size. As your supply
chain partner, we arm you with the resources you need to make your supply chain more efficient. Our team
works with your team on a daily basis to help you solve problems and achieve goals. This team approach has
helped CLS customers to succeed and we can do the same for you.

NAICS Codes:
423610 Electrical Apparatus and Equipment, Wiring Supplies, and Related Equipment Merchant
Wholesalers
423510 Metal Service Centers and Other Metal Merchant Wholesalers
423720 Plumbing and Heating Equipment and Supplies (Hydronics) Merchant Wholesalers

Certifications
MBE (KRVPQAL, State of Tennessee Up-MRX and FJW), WBE (HQOLT),
WOSB, DOT (TDOT, MDOT, ALDOT, SCDOT, NCDOT, and VDOT), LOSB,
SBE, and LSB Certified
Some of Our Products Include:
. Boxes & Covers
. Conduit & Raceway
. Fittings
. Fuses
. Lamp & Ballasts
. Lighting Controls & Timers
. Lighting Fixtures
. Personal Safety
. Pipes
. Power Distribution
. Terminations Ground & Splices
. Tools & Testers
. Wire, Cords & Cable
. Wiring Devices
. Valves

Industry/Entity Type

Business

Contact Information for Business Card

Marianne T. Holloway - President/CEO
4728 Quillon Ave., Memphis, TN 38127
901-555-0147 office, 901-555-0182 fax, 901-555-0163 cell
mtholloway@clsllc-example.com - www.clsincorp-example.com

```html
<!DOCTYPE html>
<html lang="en">
<head>
<meta charset="utf-8">
<title>Copperfield Lantern &amp; Spark — Business Card</title>
<link rel="stylesheet" href="https://fonts.googleapis.com/css2?family=Cormorant+SC:wght@500&family=Arimo:wght@400&display=swap">
<style>
  :root {
    --page: #e7e5df;
    --card-white: #ffffff;
    --ink: #1b1b1b;
    --contact: #3a3a3a;
    --panel-dark: #232323;
    --panel-mid: #3c3c3c;
    --accent: #b9bc1c;
    --title-grey: #b8b8b8;
    --olive-light: #b3b31a;
    --olive-dark: #7f7f08;
  }
  * { box-sizing: border-box; margin: 0; padding: 0; }
  html, body { width: 1200px; height: 950px; overflow: hidden; }
  body {
    background: var(--page);
    display: flex;
    flex-direction: column;
    align-items: center;
    justify-content: center;
    gap: 50px;
  }
  .card {
    width: 700px;
    height: 400px;
    position: relative;
    overflow: hidden;
    box-shadow: 0 6px 18px rgba(0,0,0,.18);
  }

  /* Front */
  .card-front { background: var(--card-white); }
  .brand {
    position: absolute;
    left: 42px;
    top: 40px;
    display: flex;
    align-items: center;
    gap: 10px;
    font-family: "Cormorant SC", Georgia, serif;
    font-weight: 500;
    font-size: 27px;
    line-height: 1.05;
    color: var(--ink);
  }
  .brand-mark { width: 14px; height: 14px; background: var(--ink); flex: none; }
  .contact {
    position: absolute;
    left: 42px;
    top: 150px;
    font-family: "Arimo", Arial, sans-serif;
    font-size: 15.5px;
    line-height: 21px;
    color: var(--contact);
    list-style: none;
  }
  .contact li { display: flex; align-items: center; gap: 8px; }
  .contact svg { width: 15px; height: 15px; fill: var(--ink); flex: none; }
  .dark-panel {
    position: absolute;
    right: 0;
    top: 0;
    width: 270px;
    height: 100%;
    background: linear-gradient(90deg, var(--panel-mid), var(--panel-dark) 70%);
  }
  .person {
    position: absolute;
    left: 0;
    top: 0;
    width: 360px;
    transform-origin: top left;
    transform: translate(140px, 380px) rotate(-90deg);
    font-family: "Cormorant SC", Georgia, serif;
    font-weight: 500;
    white-space: nowrap;
  }
  .person-name { display: block; font-size: 31px; line-height: 38px; color: var(--accent); letter-spacing: .3px; }
  .person-title { display: block; font-size: 22px; line-height: 30px; color: var(--title-grey); }

  /* Back */
  .card-back {
    background: linear-gradient(100deg, var(--olive-light), var(--olive-dark));
    display: flex;
    flex-direction: column;
    align-items: center;
    justify-content: center;
    gap: 18px;
  }
  .back-brand {
    font-family: "Cormorant SC", Georgia, serif;
    font-weight: 500;
    font-size: 40px;
    color: var(--ink);
    text-align: center;
    line-height: 1.05;
  }
  .back-url {
    font-family: "Arimo", Arial, sans-serif;
    font-size: 18px;
    letter-spacing: 1px;
    color: var(--ink);
  }
</style>
</head>
<body>

<section class="card card-front">
  <div class="brand">
    <span class="brand-mark"></span>
    <span>Copperfield Lantern<br>&amp; Spark</span>
  </div>

  <ul class="contact">
    <li>4728 Quillon Ave.</li>
    <li>Memphis, TN 38127</li>
    <li>
      <svg viewBox="0 0 16 16" aria-label="Office"><path d="M2 6c0-2 2-3 6-3s6 1 6 3v1h-3V6H5v1H2zM4 8h8l2 6H2z"/></svg>
      901-555-0147
    </li>
    <li>
      <svg viewBox="0 0 16 16" aria-label="Fax"><path d="M4 1h7v4h3v9H2V5h2zM5 2v4h5V2zM4 8v1h8V8zm0 2v1h8v-1z"/></svg>
      901-555-0182
    </li>
    <li>
      <svg viewBox="0 0 16 16" aria-label="Cell"><path d="M4 1h8v14H4zM5.5 3v9h5V3z"/></svg>
      901-555-0163
    </li>
    <li>
      <svg viewBox="0 0 16 16" aria-label="Email"><path d="M1 3h14v10H1zM2 4l6 5 6-5z" fill-rule="evenodd"/></svg>
      mtholloway@clsllc-example.com
    </li>
    <li>
      <svg viewBox="0 0 16 16" aria-label="Web"><circle cx="8" cy="8" r="7"/><path d="M1.5 8h13M8 1c3 3 3 11 0 14M8 1c-3 3-3 11 0 14" stroke="#fff" stroke-width="1" fill="none"/></svg>
      www.clsincorp-example.com
    </li>
  </ul>

  <div class="dark-panel">
    <div class="person">
      <span class="person-name">Marianne T. Holloway</span>
      <span class="person-title">President/CEO</span>
    </div>
  </div>
</section>

<section class="card card-back">
  <div class="back-brand">Copperfield Lantern<br>&amp; Spark, Inc.</div>
  <div class="back-url">www.clsincorp-example.com</div>
</section>

</body>
</html>
```